Tirolex

We need a business card for our company is a holding for different business all are different we try to have some air of relax and fun in our projects we add pictures of the office to give you an idea od the mood of the business

Business

```html
<!DOCTYPE html>
<html lang="en">
<head>
<meta charset="utf-8">
<title>Tirolex – Business Card</title>
<link rel="stylesheet" href="https://fonts.googleapis.com/css2?family=Roboto:wght@400;500;700&display=swap">
<style>
  :root {
    --backdrop: #ececec;
    --card: #ffffff;
    --sun-yellow: #f4df0c;
    --bark-brown: #5a3410;
    --ink: #1c1c1c;
  }
  * { margin: 0; padding: 0; box-sizing: border-box; }
  html, body {
    width: 1200px;
    height: 984px;
    overflow: hidden;
    background: var(--backdrop);
    font-family: "Roboto", Arial, sans-serif;
  }
  .business-card {
    position: absolute;
    left: 380px;
    top: 107px;
    width: 440px;
    height: 770px;
    background: var(--card);
    box-shadow: 0 6px 24px rgba(0,0,0,0.12);
    overflow: hidden;
  }
  .brand {
    position: absolute;
    left: 60px;
    top: 190px;
    display: flex;
    align-items: center;
    gap: 14px;
  }
  .brand-mark {
    width: 30px;
    height: 30px;
    background: var(--sun-yellow);
  }
  .brand-name {
    font-weight: 700;
    font-size: 54px;
    letter-spacing: -1px;
    color: var(--bark-brown);
  }
  .name-band {
    position: absolute;
    left: 0;
    top: 500px;
    width: 440px;
    height: 46px;
  }
  .holder-name {
    position: absolute;
    right: 52px;
    top: 509px;
    font-size: 22px;
    font-weight: 500;
    line-height: 28px;
    color: var(--bark-brown);
  }
  .contact-list {
    position: absolute;
    left: 150px;
    top: 588px;
    list-style: none;
    font-size: 22px;
    line-height: 28px;
    color: var(--ink);
  }
  .contact-item {
    display: flex;
    align-items: center;
    gap: 10px;
    margin-bottom: 16px;
  }
  .contact-icon { width: 20px; height: 20px; flex: none; }
</style>
</head>
<body>
  <article class="business-card">
    <div class="brand">
      <span class="brand-mark"></span>
      <span class="brand-name">Tirolex</span>
    </div>

    <svg class="name-band" viewBox="0 0 440 46" preserveAspectRatio="none" aria-hidden="true">
      <rect x="0" y="0" width="440" height="46" fill="var(--sun-yellow)"/>
      <path d="M0 0 L40 0 Q18 22 30 46 L0 46 Z" fill="var(--bark-brown)"/>
      <path d="M440 0 L400 0 Q420 22 408 46 L440 46 Z" fill="var(--bark-brown)"/>
    </svg>
    <p class="holder-name">Name Here</p>

    <ul class="contact-list">
      <li class="contact-item">
        <svg class="contact-icon" viewBox="0 0 20 20" aria-hidden="true">
          <circle cx="10" cy="10" r="10" fill="var(--ink)"/>
          <path d="M7 5 L9 7.5 L8 9 Q9.5 11.5 11 12 L12.5 11 L15 13 L13.5 15 Q8 14.5 5.5 8 Z" fill="#fff"/>
        </svg>
        <span>+00 412 7730 56</span>
      </li>
      <li class="contact-item">
        <svg class="contact-icon" viewBox="0 0 20 20" aria-hidden="true">
          <circle cx="10" cy="10" r="9" fill="none" stroke="var(--ink)" stroke-width="1.6"/>
          <rect x="5" y="6.5" width="10" height="7" fill="none" stroke="var(--ink)" stroke-width="1.3"/>
          <path d="M5 6.5 L10 10.5 L15 6.5" fill="none" stroke="var(--ink)" stroke-width="1.3"/>
        </svg>
        <span>hola@tirolexhq.com</span>
      </li>
    </ul>
  </article>
</body>
</html>
```